Kestrel Signs Facebook Banner Design

Design a facebook banner for a sign company. I would like to have a modern approach to it.

Product Offering:
Signs
Banners
Decals
Commercial Wraps

```html
<!DOCTYPE html>
<html lang="en">
<head>
<meta charset="utf-8">
<title>Kestrel Signs – Facebook Banner</title>
<link href="https://fonts.googleapis.com/css2?family=Audiowide&family=Poppins:wght@500;700&display=swap" rel="stylesheet">
<style>
  :root {
    --stage: #666666;
    --paper: #f6f6f6;
    --paper-light: #fbfbfb;
    --white: #ffffff;
    --brand-red: #e8363c;
    --brand-grey: #48484b;
    --line-light: rgba(255, 255, 255, 0.45);
    --shadow: rgba(0, 0, 0, 0.12);
  }
  * { margin: 0; padding: 0; box-sizing: border-box; }
  html, body {
    width: 1200px;
    height: 684px;
    overflow: hidden;
    background: var(--stage);
  }
  .canvas {
    position: relative;
    width: 1200px;
    height: 684px;
    background: var(--stage);
  }
  .banner {
    position: absolute;
    left: 98.6px;
    top: 132.9px;
    width: 1200px;
    height: 500px;
    transform: scale(0.8357);
    transform-origin: 0 0;
    overflow: hidden;
    background: var(--paper);
  }
  .banner__texture {
    position: absolute;
    inset: 0;
    background: linear-gradient(90deg, #eeeeee 0%, var(--paper) 45%, var(--paper-light) 100%);
  }
  .banner__shapes {
    position: absolute;
    inset: 0;
    width: 1200px;
    height: 500px;
  }
  .shape-soft { filter: drop-shadow(0 4px 10px var(--shadow)); }
  .tile { fill: var(--brand-red); }
  .tile__rule { fill: none; stroke: var(--line-light); stroke-width: 1; }
  .panel { fill: var(--white); }

  .label {
    position: absolute;
    transform: translate(-50%, -50%);
    text-align: center;
    white-space: nowrap;
  }
  .brand-name {
    font-family: "Poppins", sans-serif;
    font-weight: 700;
    color: var(--brand-grey);
    font-size: 50px;
    line-height: 1.0;
    letter-spacing: 1px;
  }
  .section-title {
    font-family: "Audiowide", sans-serif;
    font-style: italic;
    font-size: 34px;
    line-height: 1;
    letter-spacing: 1px;
  }
  .section-title--accent { color: var(--brand-red); }
  .section-title--base { color: var(--brand-grey); }
  .product {
    font-family: "Poppins", sans-serif;
    font-weight: 500;
    font-size: 26px;
    line-height: 1.35;
    color: var(--white);
  }
</style>
</head>
<body>
<main class="canvas">
  <section class="banner" aria-label="Kestrel Signs product offering banner">
    <div class="banner__texture" role="img" aria-label="Soft light grey dotted background texture"></div>

    <svg class="banner__shapes" viewBox="0 0 1200 500" aria-hidden="true">
      <!-- brand panel -->
      <polygon class="panel shape-soft" points="279,-6 534,249 279,504 24,249"/>
      <!-- heading panel -->
      <polygon class="panel shape-soft" points="553,-4 1117,-4 832,283"/>

      <!-- product tiles -->
      <g class="shape-soft">
        <polygon class="tile" points="676,138 822,284 676,430 530,284"/>
        <polygon class="tile__rule" points="676,152 808,284 676,416 544,284"/>

        <polygon class="tile" points="831,291 977,437 831,583 685,437"/>
        <polygon class="tile__rule" points="831,305 963,437 831,569 699,437"/>

        <polygon class="tile" points="988,138 1134,284 988,430 842,284"/>
        <polygon class="tile__rule" points="988,152 1120,284 988,416 856,284"/>

        <polygon class="tile" points="1141,-15 1287,131 1141,277 995,131"/>
        <polygon class="tile__rule" points="1141,-1 1273,131 1141,263 1009,131"/>
      </g>
    </svg>

    <div class="label brand-name" style="left:261px; top:270px;">KESTREL<br>SIGNS</div>

    <div class="label section-title section-title--accent" style="left:827px; top:72px;">PRODUCT</div>
    <div class="label section-title section-title--base" style="left:828px; top:115px;">OFFERING</div>

    <div class="label product" style="left:676px; top:284px;">SIGNS</div>
    <div class="label product" style="left:831px; top:437px;">BANNERS</div>
    <div class="label product" style="left:988px; top:286px;">COMMERCIAL<br>WRAPS</div>
    <div class="label product" style="left:1134px; top:128px;">DECALS</div>
  </section>
</main>
</body>
</html>
```